ALPINE Institute for Advancement and Practice in Operations

We need a Christmas card containing the following elements :
- text : " Happy Holidays! We wish good health for 2018.

We also take the opportunity to invite you to the inaugural ceremony of our training centre on the 17th April 2018. Save the date! "

- words/drawings with the following topics :
- surgery
- training
- excellence
- precision (especially Swiss precision)

- touch of humour
- modernity
- our logo
- photo of the centre
- format : A4 folded (landscape orientation)

Target Market(s)

Clients / Surgeons / Delegates / Suppliers

Industry/Entity Type

Training

Font styles to use
Sans Serif

Colors
f04a50
ec1f27
ffffff

Requirements
Must have
• color red (C0, M90, J73, N100)
Should not have
• no shocking images (even if surgical domain)

```html
<!DOCTYPE html>
<html lang="en">
<head>
<meta charset="utf-8">
<title>ALPINE Institute – Season's Greetings 2018</title>
<link rel="stylesheet" href="https://fonts.googleapis.com/css2?family=Questrial&family=Roboto:wght@400&display=swap">
<style>
  :root {
    --red: #ec1f27;
    --red-soft: #f04a50;
    --white: #ffffff;
    --panel: #f1f1f1;
    --ink: #3a3a3a;
    --photo-light: #eef2f5;
    --photo-mid: #b9c2c9;
    --photo-dark: #4b545b;
  }
  * { margin: 0; padding: 0; box-sizing: border-box; }
  html, body {
    width: 1200px;
    height: 849px;
    overflow: hidden;
    background: var(--red);
  }
  .card {
    position: relative;
    width: 1200px;
    height: 849px;
    background: var(--red);
    overflow: hidden;
    font-family: "Questrial", sans-serif;
    color: var(--white);
  }
  .doodle-pattern {
    position: absolute;
    inset: 0;
    background: var(--red);
  }
  .shapes {
    position: absolute;
    inset: 0;
    width: 1200px;
    height: 849px;
  }
  .brand-name {
    position: absolute;
    left: 752px;
    top: 329px;
    font-family: "Roboto", sans-serif;
    font-weight: 400;
    font-size: 11px;
    line-height: 16px;
    letter-spacing: 0.1px;
    text-transform: uppercase;
    color: var(--ink);
    white-space: nowrap;
  }
  .brand-mark {
    position: absolute;
    left: 990px;
    top: 331px;
    width: 34px;
    height: 34px;
    background: var(--red);
  }
  .greeting {
    position: absolute;
    left: 628px;
    top: 492px;
    width: 540px;
    font-size: 15px;
    line-height: 41px;
    letter-spacing: 0.2px;
    white-space: nowrap;
  }
  .greeting .lg { font-size: 24px; }
  .greeting .xl { font-size: 30px; }
</style>
</head>
<body>
<main class="card">
  <div class="doodle-pattern" role="img" aria-label="Faint outline pattern of Christmas doodles: stockings, gingerbread men, snowflakes, candy canes, gifts and fir sprigs"></div>

  <svg class="shapes" viewBox="0 0 1200 849">
    <defs>
      <linearGradient id="centre-photo-tone" x1="0" y1="0" x2="1" y2="1">
        <stop offset="0" stop-color="#4b545b"/>
        <stop offset="0.35" stop-color="#b9c2c9"/>
        <stop offset="0.7" stop-color="#eef2f5"/>
        <stop offset="1" stop-color="#b9c2c9"/>
      </linearGradient>
    </defs>

    <g class="soft-domes" fill="rgba(255,255,255,0.1)">
      <path d="M100,240 A143.5,143.5 0 0 1 363,240 Z"/>
      <path d="M838,240 A182.5,182.5 0 0 1 1140,240 Z"/>
      <path d="M264,584 A178,178 0 0 0 577,584 Z"/>
    </g>

    <path class="centre-photo" role="img" aria-label="Photo of the bright, modern surgical training centre with rows of operating tables and monitors"
          d="M50,328 L440,328 C530,328 584,420 584,506 L190,506 C100,506 50,420 50,328 Z"
          fill="url(#centre-photo-tone)"/>

    <path class="brand-panel"
          d="M623,420 C623,340 680,281 750,281 L1147,281 C1147,360 1090,420 1020,420 Z"
          fill="#f1f1f1"/>
  </svg>

  <p class="brand-name">Alpine Institute for Advancement<br>and Practice in Operations</p>
  <span class="brand-mark"></span>

  <p class="greeting">
    <span class="lg">Happy Holidays!</span> We wish <span class="lg">good health for 2018.</span><br>
    We also take the opportunity to invite you to the<br>
    inaugural ceremony of <span class="xl">our training centre</span><br>
    on the <span class="lg">17th April 2018. Save the date!</span>
  </p>
</main>
</body>
</html>
```